Tolvane Vitamins Sign

I need to make a sign that looks like a vintage metal sign like you would find in an old pharmacy. I'm attaching a few examples of the look and feel. The text is attached in the word file

```html
<!DOCTYPE html>
<html lang="en">
<head>
<meta charset="utf-8">
<title>Tolvane Vitamins Sign</title>
<link href="https://fonts.googleapis.com/css2?family=Ultra&display=swap" rel="stylesheet">
<style>
  :root {
    --backdrop: #cdcdcd;
    --rust-light: #8a4214;
    --rust-mid: #72330d;
    --rust-dark: #531f06;
    --cream: #f1e3cb;
    --gold: #e8b43a;
    --rule: #e6d2b4;
  }
  html, body {
    margin: 0;
    padding: 0;
    width: 1200px;
    height: 1200px;
    overflow: hidden;
    background: var(--backdrop);
  }
  .sign {
    position: absolute;
    left: 0;
    top: 200px;
    width: 1200px;
    height: 800px;
    display: block;
  }
  .sign-type {
    font-family: "Ultra", serif;
  }
  .brand-name { fill: var(--cream); }
  .tagline { fill: var(--gold); }
  .rule { stroke: var(--rule); stroke-width: 1.5; }
  .rule-bold { stroke: var(--rule); stroke-width: 3; }
</style>
</head>
<body>
<svg class="sign" viewBox="0 0 1200 800" xmlns="http://www.w3.org/2000/svg">
  <defs>
    <radialGradient id="rust-plate" cx="50%" cy="50%" r="70%">
      <stop offset="0%" stop-color="var(--rust-light)"/>
      <stop offset="65%" stop-color="var(--rust-mid)"/>
      <stop offset="100%" stop-color="var(--rust-dark)"/>
    </radialGradient>
    <radialGradient id="flourish-tone" cx="50%" cy="50%" r="50%">
      <stop offset="0%" stop-color="var(--cream)" stop-opacity="0.45"/>
      <stop offset="100%" stop-color="var(--cream)" stop-opacity="0"/>
    </radialGradient>
  </defs>

  <rect class="plate" x="0" y="0" width="1200" height="800" fill="url(#rust-plate)"/>

  <g class="corner-flourishes">
    <rect x="37" y="16" width="183" height="187" fill="url(#flourish-tone)" role="img" aria-label="Ornamental scroll flourish, top left corner"/>
    <rect x="980" y="16" width="183" height="187" fill="url(#flourish-tone)" role="img" aria-label="Ornamental scroll flourish, top right corner"/>
    <rect x="37" y="597" width="183" height="187" fill="url(#flourish-tone)" role="img" aria-label="Ornamental scroll flourish, bottom left corner"/>
    <rect x="980" y="597" width="183" height="187" fill="url(#flourish-tone)" role="img" aria-label="Ornamental scroll flourish, bottom right corner"/>
  </g>

  <g class="frame-rules">
    <line class="rule" x1="233" y1="52" x2="950" y2="52"/>
    <line class="rule" x1="233" y1="760" x2="950" y2="760"/>
    <line class="rule" x1="60" y1="215" x2="60" y2="577"/>
    <line class="rule" x1="1137" y1="215" x2="1137" y2="577"/>
  </g>

  <g class="top-tagline">
    <line class="rule-bold" x1="164" y1="183" x2="295" y2="183"/>
    <line class="rule-bold" x1="901" y1="183" x2="1035" y2="183"/>
    <text class="sign-type tagline" x="320" y="199" font-size="44" textLength="560" lengthAdjust="spacingAndGlyphs">TRUSTED FOR AGES</text>
  </g>

  <g class="brand-name-block">
    <text class="sign-type brand-name" x="130" y="450" font-size="298" textLength="950" lengthAdjust="spacingAndGlyphs">TOLVANE</text>
    <text class="sign-type brand-name" x="166" y="605" font-size="150" textLength="862" lengthAdjust="spacingAndGlyphs">VITAMINS</text>
  </g>

  <g class="bottom-tagline">
    <line class="rule-bold" x1="135" y1="651" x2="309" y2="651"/>
    <line class="rule-bold" x1="897" y1="651" x2="1066" y2="651"/>
    <text class="sign-type tagline" x="322" y="665" font-size="38" textLength="562" lengthAdjust="spacingAndGlyphs">REMEDIES OF THE AGES</text>
  </g>
</svg>
</body>
</html>
```